Clean business card with logo provided

I want a card that will stand out among the masses. I need the color and image to show professionalism and yet have a family appeal showing that I only deal with win/win scenarios. The back of the card will be used to take notes about the individual so I can use that in my database entry. I like modern design but need professionalism in it also. It needs to fit my "clean, safe, and affordable housing" motto. I need to be able to write on the file and update the card details for my employees.

Target Market(s)

Investors looking to make investment income through real estate

Industry/Entity Type

Real Estate

Contact Information for Business Card

Troy Vandemark
blank address, city, st, zip code
480-555-0147
troyvandemark@quillrentals.example
www.quillrentals.example

Font styles to use
Sans Serif

Requirements
Must have
• I would like the back of the card to have lines for info. example
• Met/Visited: Date:
• Interets:
Nice to have
• I want the cards color to match the logo background color. Font with details to be san serif and black. I want the card rectangular with square corners. Standard business card size. I would like to see cards designed with both images to see which i prefer more.

```html
<!DOCTYPE html>
<html lang="en">
<head>
<meta charset="utf-8">
<title>Quill Rentals LLC – Business Card</title>
<link rel="stylesheet" href="https://fonts.googleapis.com/css2?family=Arimo:wght@400;700&family=Open+Sans:wght@400;600&display=swap">
<style>
  :root {
    --teal: #00b9cd;
    --teal-deep: #00a9bd;
    --ink: #0d0d0d;
    --paper: #ffffff;
    --backdrop: #e9e6e1;
    --rule: #333333;
  }
  * { box-sizing: border-box; margin: 0; padding: 0; }
  html, body {
    width: 1200px; height: 892px; overflow: hidden;
    background: var(--backdrop);
    font-family: "Arimo", Arial, sans-serif;
  }
  .sheet {
    width: 1200px; height: 892px;
    display: flex; flex-direction: column; align-items: center; justify-content: center; gap: 32px;
  }
  .card {
    position: relative; width: 700px; height: 400px; overflow: hidden;
    box-shadow: 0 6px 18px rgba(0,0,0,.18);
  }

  /* Front */
  .card-front { background: linear-gradient(160deg, var(--teal) 0%, var(--teal-deep) 100%); }
  .front-corner { position: absolute; inset: 0; }
  .front-brand {
    position: absolute; top: 38px; right: 44px; text-align: right; color: var(--paper);
  }
  .brand-name {
    font-family: "Arimo", Arial, sans-serif; font-weight: 400;
    font-size: 42px; letter-spacing: 6px; line-height: 1;
  }
  .brand-tagline {
    font-family: "Open Sans", Arial, sans-serif; font-size: 13px; margin-top: 10px; letter-spacing: .3px;
  }
  .holder {
    position: absolute; left: 42px; top: 150px;
    font-weight: 700; font-size: 38px; color: var(--ink);
  }
  .contact-list {
    position: absolute; left: 42px; top: 212px; list-style: none; color: var(--ink);
    font-size: 20px; line-height: 1.55;
  }
  .contact-list li { display: flex; align-items: center; gap: 12px; }
  .contact-icon { width: 16px; height: 16px; flex: none; }

  /* Back */
  .card-back { background: var(--paper); }
  .back-band {
    position: absolute; left: 0; top: 0; width: 100%; height: 232px; background: var(--ink);
    border-bottom: 5px solid var(--teal);
  }
  .back-brand { position: absolute; left: 48px; top: 50px; color: var(--teal); }
  .back-brand .brand-name { font-size: 64px; letter-spacing: 10px; }
  .back-brand .brand-tagline { font-size: 17px; margin-top: 18px; }
  .notes {
    position: absolute; left: 44px; right: 40px; top: 262px;
    display: grid; grid-template-columns: 250px 1fr; row-gap: 8px; align-items: end;
  }
  .notes dt { font-weight: 700; font-size: 25px; color: var(--ink); line-height: 1.2; }
  .notes dd { border-bottom: 2px solid var(--rule); height: 26px; }
</style>
</head>
<body>
<main class="sheet">

  <section class="card card-front" aria-label="Business card front">
    <svg class="front-corner" viewBox="0 0 700 400" width="700" height="400" aria-hidden="true">
      <polygon points="330,400 700,215 700,400" fill="var(--paper)"/>
      <line x1="330" y1="400" x2="700" y2="215" stroke="var(--ink)" stroke-width="3"/>
    </svg>
    <div class="front-brand">
      <div class="brand-name">QUILL RENTALS LLC</div>
      <div class="brand-tagline">Providing clean, safe, and affordable housing</div>
    </div>
    <h1 class="holder">Troy Vandemark</h1>
    <ul class="contact-list">
      <li>
        <svg class="contact-icon" viewBox="0 0 16 16" aria-hidden="true"><rect width="16" height="16" fill="var(--ink)"/><path d="M5 3.5l2 2-1 1.2c.6 1.3 1.7 2.4 3 3l1.2-1 2 2-1.3 1.6C7.5 12 4 8.5 3.7 5z" fill="var(--paper)"/></svg>
        480-555-0147
      </li>
      <li>
        <svg class="contact-icon" viewBox="0 0 16 16" aria-hidden="true"><rect width="16" height="16" fill="var(--ink)"/><circle cx="8" cy="8" r="4.6" fill="none" stroke="var(--paper)" stroke-width="1.2"/><path d="M3.4 8h9.2M8 3.4c-2 2.6-2 6.6 0 9.2M8 3.4c2 2.6 2 6.6 0 9.2" fill="none" stroke="var(--paper)" stroke-width="1"/></svg>
        www.quillrentals.example
      </li>
      <li>
        <svg class="contact-icon" viewBox="0 0 16 16" aria-hidden="true"><rect width="16" height="16" fill="var(--ink)"/><rect x="3" y="4.5" width="10" height="7" fill="none" stroke="var(--paper)" stroke-width="1.2"/><path d="M3 4.5l5 4 5-4" fill="none" stroke="var(--paper)" stroke-width="1.2"/></svg>
        troyvandemark@quillrentals.example
      </li>
      <li>
        <svg class="contact-icon" viewBox="0 0 16 16" aria-hidden="true"><rect width="16" height="16" fill="var(--ink)"/><path d="M8 13s-3.6-4-3.6-6.4a3.6 3.6 0 017.2 0C11.6 9 8 13 8 13z" fill="var(--paper)"/><circle cx="8" cy="6.6" r="1.3" fill="var(--ink)"/></svg>
        742 Cedar Row, Maple Grove, IL 60412
      </li>
    </ul>
  </section>

  <section class="card card-back" aria-label="Business card back">
    <div class="back-band">
      <div class="back-brand">
        <div class="brand-name">QUILL RENTALS LLC</div>
        <div class="brand-tagline">Providing clean, safe, and affordable housing</div>
      </div>
    </div>
    <dl class="notes">
      <dt>Met/Visited: Date:</dt><dd></dd>
      <dt>Interets:</dt><dd></dd>
      <dt>Problems:</dt><dd></dd>
    </dl>
  </section>

</main>
</body>
</html>
```